We need a .psd design for a store we are creating called Bright Pouches. I will need only the main home page designed.

The store will be an eCommerce website that sells custom printed men's wallets. Customers will come onto the website and be able to upload their own images or add text to the front, back and inside of the wallet. We will initially be launching with one wallet style and will be expanding our range in the future for now the only images of a wallet on the website should be of the style attached.

There will be multiple templates that a customer can choose and edit the design of so there will effectively be a large number of products on display in the store. However, on the homepage there should just be a couple of featured products and the main emphasis should be on the features of the wallet/website and links to other areas of the website (customise your own wallet, edit our templates, bespoke designer wallets).

For the styling of the website, it needs to be funky and fresh with lots of colour. The logo of the website is attached and the styling should mirror the logo style.

The main features of the website should be on the home page. These features are:
- 5 year money back guarantee on wallet
- High quality, durable leather, made to last
- customer can upload photo and edit them online with our online picture editor
- 3d mockup of the wallet as you are designing it to show what it looks like with custom images on
- Edit any of our ready made wallet designs

Features of this wallet may be used as well - these can be viewed on "Image 6" of the attached product image .psd files.

Attached are the logo for the website and the wallet product photos. The product photos are provided in .psd format and have smart objects so that you can add any image to the front/inside of the wallets for any images on the website you create. Fee free to edit them and use them for banner images and feature images however you feel necessary.

The term "what does you wallet say about you" should be used as this is a tagline for most of the marketing - based on the fact that the wallets are personalised to each individual they will show off that individuals personality and what they like.

The eventual website will be hosted on cartnest and will more than likely use the "StallKit" theme. This is a highly adaptable theme and examples of the layout styles for the homepage can be found here: http://reef.lindolayouts.example/cartnest/stallkit-intro/?storefront=pixora-assets however i do not want you to just copy a ready made template and stick some stock photos in - I only want one page designing here, put the effort in with the banners and feature images and you'll win this.

Any images that you create for hero sliders/banners should be provided in .psd format so that they can be edited as necessary in the future. A newsletter popup should also be designed as the website will have postwren integration, the newsletter popup is a 500 x 750 image that pops up with a message saying "subscribe to our newsletter and get 10% off your next order".

There should also be an area of the page that has customer testimonials.

Target Market(s)

Males, aged 18 - 45

Industry/Entity Type

Retail

Number of Pages Required

1 page

Font styles to use
Serif
Decorative
Script

Colors

Designer to choose colors to be used in the design.

Requirements
Must have
• Vibrant and uplifting feel to the website
• Design which reflects the logo
• Features of the website and wallets should feature prominently on the homepage (but not in banner/hero image)
Nice to have
• hipster/geek/easygoing vibe
• Images that have used the wallet .psd files and have different designs on them showing customers that anything can be printed on the wallets
• Custom images/styles for the featured images and main banner.
Should not have
• - Boring images
• - Stock Photos
• - Mundane feel
• - Square block style images - try putting images in circles or geometric shapes with colours, just adding a stock photo to some "lorem Ipsum" text will not win you this contest

```html
<!DOCTYPE html>
<html lang="en">
<head>
<meta charset="utf-8">
<title>Bright Pouches – Custom Printed Wallets</title>
<link href="https://fonts.googleapis.com/css2?family=Montserrat:wght@500;600;700;800;900&family=Arimo:ital,wght@0,700;1,400&display=swap" rel="stylesheet">
<style>
  :root {
    --ink: #1f2630;
    --ink-dark: #1b2128;
    --accent-red: #e0352b;
    --accent-green: #1fa24e;
    --offer-green: #1fc46c;
    --accent-yellow: #f3d81e;
    --accent-blue: #1a9ad6;
    --accent-pink: #d93a8c;
    --paper: #ffffff;
    --tile: #ececec;
    --band: #efefef;
    --line: #3a3a3a;
    --dim: rgba(40, 40, 40, 0.12);
  }
  * { box-sizing: border-box; margin: 0; padding: 0; }
  html, body { width: 1200px; height: 2324px; overflow: hidden; background: var(--paper); }
  body { font-family: "Montserrat", Arial, sans-serif; color: var(--ink); }
  .page { position: relative; width: 1200px; height: 2324px; overflow: hidden; background: var(--paper); }
  .abs { position: absolute; }

  /* header */
  .site-header { position: absolute; left: 0; top: 0; width: 1200px; height: 106px; border-bottom: 1px solid #9a9a9a; }
  .brand { position: absolute; left: 107px; top: 24px; display: flex; align-items: center; gap: 14px; }
  .brand-dot { width: 58px; height: 58px; border-radius: 50%; background: var(--accent-green); }
  .brand-name { font-weight: 800; font-size: 26px; color: var(--ink); letter-spacing: -0.3px; }
  .main-nav { position: absolute; top: 46px; left: 615px; font-weight: 700; font-size: 12.5px; }
  .main-nav a { position: absolute; white-space: nowrap; color: var(--ink); text-decoration: none; }
  .main-nav a.current { color: var(--accent-red); }

  /* hero */
  .hero-shapes { position: absolute; left: 0; top: 106px; width: 1200px; height: 520px; }
  .hero-title { position: absolute; left: 549px; top: 122px; font-weight: 900; font-size: 38px; letter-spacing: -0.5px; }
  .photo-print { position: absolute; left: 140px; top: 282px; width: 140px; height: 190px; background: #f4f4f4; border: 8px solid #fafafa; box-shadow: 0 2px 6px rgba(0,0,0,.25); transform: rotate(-9deg); }
  .photo-print span { display: block; width: 100%; height: 80%; background: linear-gradient(135deg, #d9b89a, #8a6a55); }
  .phone-mock { position: absolute; left: 930px; top: 197px; width: 111px; height: 386px; border-radius: 18px; background: linear-gradient(180deg, #f2f2f2, #dcdcdc); border: 2px solid #c9c9c9; }
  .swirl { position: absolute; border-radius: 46% 54% 40% 60% / 55% 45% 55% 45%; }
  .swirl-hero { left: 1093px; top: 139px; width: 120px; height: 195px; background: linear-gradient(160deg, var(--accent-red), var(--accent-blue) 40%, var(--accent-yellow) 70%, var(--accent-green)); }

  .hero-links { position: absolute; top: 628px; left: 0; width: 1200px; }
  .hero-link { position: absolute; width: 279px; height: 66px; background: var(--ink-dark); color: var(--accent-yellow); font-weight: 800; font-size: 19px; line-height: 22px; text-align: center; padding-top: 11px; overflow: hidden; }
  .hero-link::before { content: ""; position: absolute; right: -10px; top: -8px; width: 70px; height: 50px; border-radius: 50%; background: var(--accent-red); opacity: .75; }
  .hero-link span { position: relative; }

  /* features */
  .features { position: absolute; top: 738px; left: 0; width: 1200px; }
  .feature { position: absolute; width: 230px; }
  .feature-icon { width: 100px; height: 100px; }
  .feature-text { margin-top: 2px; font-size: 15px; line-height: 19px; font-weight: 600; text-transform: uppercase; letter-spacing: -0.2px; }
  .feature-text b { font-weight: 800; }

  .section-title { position: absolute; left: 0; width: 1200px; text-align: center; font-weight: 800; font-size: 19px; }
  .product-card { position: absolute; top: 1003px; width: 303px; height: 221px; background: var(--tile); }

  .wallet-diagram { position: absolute; left: 0; top: 1270px; width: 1200px; height: 380px; }

  /* testimonials */
  .testimonials { position: absolute; left: 0; top: 1672px; width: 1200px; height: 488px; background: var(--band); }
  .swirl-left { left: -30px; top: 1750px; width: 251px; height: 440px; background: linear-gradient(170deg, var(--accent-red), var(--accent-yellow) 35%, #bdbdbd 55%, var(--accent-blue) 75%, var(--accent-red)); }
  .swirl-right { left: 978px; top: 1609px; width: 250px; height: 252px; background: linear-gradient(200deg, var(--accent-red), var(--accent-blue) 40%, var(--accent-yellow) 70%, #bdbdbd); }
  .quote { position: absolute; left: 289px; width: 604px; font-family: "Arimo", Arial, sans-serif; font-size: 15px; line-height: 19px; color: #2a2a2a; }
  .quote-name { font-weight: 700; font-size: 15.5px; }
  .quote-text { font-style: italic; font-weight: 400; }

  /* footer */
  .site-footer { position: absolute; left: 0; top: 2160px; width: 1200px; height: 164px; background: var(--paper); }
  .footer-nav { position: absolute; top: 59px; left: 0; width: 1200px; display: flex; justify-content: center; align-items: center; gap: 19px; font-weight: 700; font-size: 11px; }
  .social { display: flex; gap: 13px; margin-left: 6px; }
  .social span { width: 20px; height: 20px; background: var(--ink); border-radius: 2px; }
  .legal { position: absolute; top: 102px; left: 0; width: 1200px; text-align: center; font-size: 10.5px; font-weight: 500; }
  .legal u { text-decoration: underline; }

  /* newsletter popup */
  .backdrop { position: absolute; inset: 0; background: var(--dim); }
  .newsletter { position: absolute; left: 227px; top: 153px; width: 746px; height: 497px; background: var(--paper); overflow: hidden; }
  .newsletter-close { position: absolute; right: 0; top: 0; width: 49px; height: 49px; background: var(--ink-dark); z-index: 2; }
  .swirl-popup-top { left: 520px; top: -20px; width: 250px; height: 290px; background: linear-gradient(200deg, var(--accent-green), var(--accent-blue) 30%, var(--accent-red) 55%, #c9c9c9 75%, var(--accent-yellow)); border-radius: 30% 0 50% 60%; }
  .swirl-popup-left { left: -40px; top: 155px; width: 255px; height: 370px; background: linear-gradient(180deg, var(--accent-yellow), var(--accent-red) 30%, var(--accent-green) 50%, #c9c9c9 70%, var(--accent-blue)); border-radius: 20% 60% 30% 40%; }
  .newsletter-heading { position: absolute; left: 0; top: 115px; width: 746px; text-align: center; font-weight: 900; font-size: 32px; line-height: 38px; color: var(--ink); }
  .newsletter-heading em { font-style: normal; color: var(--offer-green); }
  .newsletter-input { position: absolute; left: 230px; top: 296px; width: 280px; height: 44px; border: 1px solid #8a8a8a; background: #fff; }
  .newsletter-submit { position: absolute; left: 230px; top: 355px; width: 280px; height: 44px; background: var(--ink-dark); color: var(--accent-yellow); font-weight: 800; font-size: 19px; text-align: center; line-height: 44px; }
</style>
</head>
<body>
<div class="page">

  <header class="site-header">
    <div class="brand"><span class="brand-dot"></span><span class="brand-name">Bright Pouches</span></div>
    <nav class="main-nav">
      <a class="current" style="left:0">HOME</a>
      <a style="left:63px">ABOUT US</a>
      <a style="left:151px">BROWSE OUR DESIGNS</a>
      <a style="left:320px">SIGN IN</a>
      <a style="left:394px">CONTACT US</a>
    </nav>
  </header>

  <svg class="hero-shapes" viewBox="0 0 1200 520" aria-hidden="true">
    <polygon points="0,49 330,100 330,300 139,490 139,330 0,300" fill="var(--accent-green)"/>
    <polygon points="973,150 1105,195 1200,150 1200,360 973,320" fill="var(--accent-yellow)"/>
  </svg>
  <div class="hero-title">funk up</div>
  <div class="photo-print" role="img" aria-label="Printed photo of a customer"><span></span></div>
  <div class="phone-mock" role="img" aria-label="Phone showing a printed wallet design"></div>
  <div class="swirl swirl-hero" role="img" aria-label="Colourful swirl ornament"></div>

  <div class="hero-links">
    <div class="hero-link" style="left:137px"><span>CUSTOMISE<br>YOUR OWN WALLET</span></div>
    <div class="hero-link" style="left:457px"><span>EDIT<br>OUR TEMPLATES</span></div>
    <div class="hero-link" style="left:777px"><span>BESPOKE<br>DESIGNER WALLETS</span></div>
  </div>

  <section class="features">
    <div class="feature" style="left:107px">
      <svg class="feature-icon" viewBox="0 0 100 100" aria-hidden="true" style="margin-left:12px">
        <ellipse cx="50" cy="50" rx="46" ry="44" fill="var(--accent-green)"/>
        <path d="M36 44 V33 a14 14 0 0 1 28 0 V44" fill="none" stroke="var(--ink)" stroke-width="5"/>
        <rect x="28" y="44" width="44" height="38" rx="4" fill="none" stroke="var(--ink)" stroke-width="5"/>
        <text x="50" y="72" text-anchor="middle" font-family="Montserrat, sans-serif" font-weight="900" font-size="22" fill="var(--ink)">5</text>
      </svg>
      <p class="feature-text"><b>5 year money-<br>back</b> guarantee<br>on wallet</p>
    </div>
    <div class="feature" style="left:292px">
      <svg class="feature-icon" viewBox="0 0 100 100" aria-hidden="true" style="margin-left:12px">
        <ellipse cx="52" cy="50" rx="44" ry="46" fill="var(--accent-yellow)"/>
        <circle cx="50" cy="50" r="30" fill="none" stroke="var(--ink)" stroke-width="5" stroke-dasharray="10 4"/>
        <circle cx="50" cy="50" r="19" fill="none" stroke="var(--ink)" stroke-width="4"/>
        <path d="M41 50 l7 7 l12 -13" fill="none" stroke="var(--ink)" stroke-width="5"/>
      </svg>
      <p class="feature-text"><b>High quality,</b><br>durable leather,<br>made to last</p>
    </div>
    <div class="feature" style="left:478px">
      <svg class="feature-icon" viewBox="0 0 100 100" aria-hidden="true" style="margin-left:22px">
        <ellipse cx="50" cy="50" rx="46" ry="44" fill="var(--accent-blue)"/>
        <path d="M28 34 L50 28 L72 34 V70 L50 76 L28 70 Z" fill="none" stroke="var(--ink)" stroke-width="5"/>
        <path d="M38 52 H60 M53 45 l7 7 l-7 7" fill="none" stroke="var(--ink)" stroke-width="5"/>
        <path d="M10 56 q40 26 80 -6" fill="none" stroke="var(--ink)" stroke-width="4"/>
      </svg>
      <p class="feature-text"><b>3D mockup</b><br>of the wallet as<br>you are designing</p>
    </div>
    <div class="feature" style="left:684px">
      <svg class="feature-icon" viewBox="0 0 100 100" aria-hidden="true" style="margin-left:20px">
        <ellipse cx="48" cy="50" rx="46" ry="44" fill="var(--accent-red)"/>
        <rect x="20" y="30" width="48" height="40" rx="3" fill="none" stroke="var(--ink)" stroke-width="5"/>
        <path d="M26 64 l12 -14 l10 10 l8 -6 l8 10" fill="none" stroke="var(--ink)" stroke-width="4"/>
        <path d="M62 50 l24 10 l-10 4 l8 10 l-5 4 l-8 -10 l-6 8 Z" fill="var(--paper)" stroke="var(--ink)" stroke-width="3.5"/>
      </svg>
      <p class="feature-text"><b>Edit</b> any of our<br>ready made<br>wallet designs</p>
    </div>
    <div class="feature" style="left:863px;width:260px">
      <svg class="feature-icon" viewBox="0 0 120 100" aria-hidden="true" style="width:120px;margin-left:50px">
        <ellipse cx="38" cy="50" rx="34" ry="36" fill="var(--accent-pink)"/>
        <rect x="48" y="16" width="62" height="44" rx="3" fill="none" stroke="var(--ink)" stroke-width="5"/>
        <rect x="16" y="40" width="40" height="38" rx="3" fill="var(--paper)" stroke="var(--ink)" stroke-width="5"/>
        <circle cx="36" cy="54" r="5" fill="var(--ink)"/>
        <path d="M26 72 q10 -14 20 0" fill="var(--ink)"/>
        <path d="M62 48 L88 26 M78 26 H88 V36" fill="none" stroke="var(--ink)" stroke-width="4"/>
      </svg>
      <p class="feature-text"><b>Upload your photo</b><br>and edit them online with<br>our online picture editor</p>
    </div>
  </section>

  <h2 class="section-title" style="top:950px">FEATURED PRODUCTS</h2>
  <div class="product-card" style="left:107px"></div>
  <div class="product-card" style="left:449px"></div>
  <div class="product-card" style="left:788px"></div>

  <svg class="wallet-diagram" viewBox="0 0 1200 380" aria-label="Wallet features diagram">
    <g fill="none" stroke="var(--line)" stroke-width="2">
      <polyline points="394,75 502,75 528,110"/>
      <line x1="344" y1="192" x2="528" y2="192"/>
      <polyline points="394,299 502,299 545,244"/>
      <polyline points="796,75 694,75 662,118"/>
      <line x1="864" y1="192" x2="678" y2="192"/>
      <polyline points="796,299 694,299 662,252"/>
    </g>
    <g role="img" aria-label="Close-up of reinforced wallet corners"><circle cx="342" cy="58" r="56" fill="var(--accent-blue)"/><circle cx="342" cy="58" r="40" fill="#3a3a3a"/></g>
    <g role="img" aria-label="Close-up showing slim wallet profile"><circle cx="284" cy="184" r="58" fill="var(--accent-red)"/><circle cx="284" cy="184" r="41" fill="#6a6a6a"/></g>
    <g role="img" aria-label="Close-up of coin compartment"><circle cx="342" cy="283" r="56" fill="var(--accent-green)"/><circle cx="342" cy="283" r="40" fill="#4a4a4a"/></g>
    <g role="img" aria-label="Close-up of luxury leather texture"><circle cx="852" cy="67" r="56" fill="var(--accent-yellow)"/><circle cx="852" cy="67" r="40" fill="#5a5a5a"/></g>
    <g role="img" aria-label="Close-up of card slots"><circle cx="918" cy="184" r="58" fill="#111"/><circle cx="918" cy="184" r="41" fill="#3c3c3c"/></g>
    <g role="img" aria-label="Close-up of note pockets"><circle cx="852" cy="294" r="56" fill="var(--accent-pink)"/><circle cx="852" cy="294" r="40" fill="#4a4a4a"/></g>
    <rect x="528" y="118" width="150" height="145" rx="8" fill="url(#walletTone)" role="img" aria-label="Wallet printed with a colourful paint design"/>
    <defs>
      <linearGradient id="walletTone" x1="0" y1="0" x2="1" y2="1">
        <stop offset="0" stop-color="#f3d81e"/><stop offset=".45" stop-color="#2f8fcf"/><stop offset=".75" stop-color="#e0352b"/><stop offset="1" stop-color="#d93a8c"/>
      </linearGradient>
    </defs>
  </svg>

  <section class="testimonials">
    <h2 class="section-title" style="top:37px">WHAT THEY SAY ABOUT US</h2>
  </section>
  <div class="swirl swirl-right" role="img" aria-label="Colourful swirl ornament"></div>
  <div class="swirl swirl-left" role="img" aria-label="Colourful swirl ornament"></div>
  <div class="quote" style="top:1755px">
    <p class="quote-name">Lorem Ipsum Dolor</p>
    <p class="quote-text">sit amet, consectetur adipiscing elit, sed do eiusmod tempor incididunt ut labore et dolore magna aliqua. Ut enim ad minim veniam, quis nostrud exercitation ullamco laboris nisi ut aliquip ex ea commodo consequat.</p>
  </div>
  <div class="quote" style="top:1878px">
    <p class="quote-name">Lorem Ipsum Dolor</p>
    <p class="quote-text">sit amet, consectetur adipiscing elit, sed do eiusmod tempor incididunt ut labore et dolore magna aliqua. Ut enim ad minim veniam, quis nostrud exercitation ullamco laboris nisi ut aliquip ex ea commodo consequat.</p>
  </div>
  <div class="quote" style="top:1998px">
    <p class="quote-name">Lorem Ipsum Dolor</p>
    <p class="quote-text">sit amet, consectetur adipiscing elit, sed do eiusmod tempor incididunt ut labore et dolore magna aliqua. Ut enim ad minim veniam, quis nostrud exercitation ullamco laboris nisi ut aliquip ex ea commodo consequat.</p>
  </div>
  <svg class="abs" style="left:584px;top:2110px" width="26" height="16" viewBox="0 0 26 16" aria-hidden="true">
    <polyline points="2,3 13,13 24,3" fill="none" stroke="var(--ink)" stroke-width="2"/>
  </svg>

  <footer class="site-footer">
    <nav class="footer-nav">
      <span>HOME</span><span>ABOUT US</span><span>BROWSE OUR DESIGNS</span><span>SIGN IN</span><span>CONTACT US</span>
      <span class="social"><span></span><span></span><span></span></span>
    </nav>
    <p class="legal"><u>Terms of Use</u> &nbsp;&amp;&nbsp; <u>Privacy Policy</u> &nbsp;© 2018 Bright Pouches • All rights reserved</p>
  </footer>

  <div class="backdrop"></div>

  <aside class="newsletter">
    <div class="swirl swirl-popup-top" role="img" aria-label="Colourful swirl ornament"></div>
    <div class="swirl swirl-popup-left" role="img" aria-label="Colourful swirl ornament"></div>
    <div class="newsletter-close">
      <svg width="49" height="49" viewBox="0 0 49 49" aria-hidden="true">
        <path d="M16 16 L33 33 M33 16 L16 33" stroke="#fff" stroke-width="2"/>
      </svg>
    </div>
    <h2 class="newsletter-heading">SUBSCRIBE TO<br>OUR NEWSLETTER<br>AND GET <em>10% OFF</em><br>YOUR NEXT ORDER</h2>
    <div class="newsletter-input"></div>
    <div class="newsletter-submit">SUBSCRIBE</div>
  </aside>

</div>
</body>
</html>
```